Design a book cover for "The Harvester's Ledger"

We need a book cover for a book titled "The Harvester's Ledger" The subtitle is "Why Machines Deliver a Shared Dividend, the Close of Levy Systems, and a Steady Treasury"
You can use one of the attached files of cover art, or come up with your own art - designer's choice!
Author's Name is Brent Hallow
We'd like the copy in the attached file "Back Cover" on the back cover, along with the copy in "About the Author" and the author's photo on the back cover.
Updates

Project Deadline Extended Reason: The deadline has been extended to give time for designers to respond to comments. Feel free to submit designs that do not use the cover art graphics attached to the brief - that art was meant as a suggestion. Added Sunday, January 15, 2017

Target Market(s)

Layperson

Font styles to use
Sans Serif

Colors
0456a4
3176b5
85abd2
0293ce
33a6d7
85cae6
1b1b1b
474747
919191

Requirements
Nice to have
• We'd like to see how the horse and rider would look on the front cover. The attached file, "Pendlewick Option", is a rough sketch. The artist is refining it, adding color, and will have the rider carrying modern technology instead of scrolls.
• We are open to all colors, but have indicated some colors we like.

```html
<!DOCTYPE html>
<html lang="en">
<head>
<meta charset="utf-8">
<title>The Harvester's Ledger — Front Cover</title>
<link href="https://fonts.googleapis.com/css2?family=Oswald:wght@400;500;600&display=swap" rel="stylesheet">
<style>
  :root {
    --stage: #d9d9d9;
    --paper: #fbfcfd;
    --sky-light: #a9dcf6;
    --sky-mid: #8fd0f1;
    --sky-deep: #7cc6ec;
    --ink: #336f96;
    --ink-soft: #4a7fa3;
    --rule: #5f8fb0;
    --gold: #f3d36a;
  }
  * { margin: 0; padding: 0; box-sizing: border-box; }
  html, body {
    width: 1200px;
    height: 1200px;
    overflow: hidden;
    background: var(--stage);
  }
  .canvas {
    position: relative;
    width: 1200px;
    height: 1200px;
    display: flex;
    align-items: center;
    justify-content: center;
  }
  .cover {
    position: relative;
    width: 780px;
    height: 1130px;
    background: var(--paper);
    overflow: hidden;
    font-family: "Oswald", "Arial Narrow", sans-serif;
    color: var(--ink);
  }
  .sky-band {
    position: absolute;
    left: 0;
    top: 0;
    width: 780px;
    height: 640px;
    background: linear-gradient(180deg,
      var(--sky-light) 0%,
      var(--sky-light) 45%,
      var(--sky-mid) 72%,
      var(--sky-deep) 88%,
      var(--paper) 100%);
  }
  .subtitle {
    position: absolute;
    top: 92px;
    left: 60px;
    right: 60px;
    text-align: center;
    font-size: 23px;
    font-weight: 500;
    line-height: 1.3;
    color: var(--ink-soft);
  }
  .title {
    position: absolute;
    top: 195px;
    left: 0;
    right: 0;
    text-align: center;
    text-transform: uppercase;
    font-weight: 600;
    line-height: 0.98;
  }
  .title-lead {
    display: flex;
    align-items: center;
    justify-content: center;
    gap: 26px;
    font-size: 80px;
    margin-bottom: 8px;
  }
  .title-lead::before,
  .title-lead::after {
    content: "";
    width: 200px;
    height: 2px;
    background: var(--rule);
    opacity: 0.7;
  }
  .title-main {
    display: block;
    font-size: 128px;
    letter-spacing: -1px;
  }
  .artwork {
    position: absolute;
    left: 270px;
    top: 690px;
    width: 240px;
    height: 190px;
    border-radius: 14px;
    background: linear-gradient(180deg, var(--sky-deep) 0%, #a8d8ef 55%, var(--gold) 100%);
  }
  .author {
    position: absolute;
    top: 955px;
    left: 0;
    right: 0;
    text-align: center;
    font-size: 64px;
    font-weight: 500;
    letter-spacing: 24px;
    padding-left: 24px;
    text-transform: uppercase;
  }
</style>
</head>
<body>
<main class="canvas">
  <section class="cover">
    <div class="sky-band" role="img" aria-label="Illustration of a soft blue cloud bank across the top of the cover"></div>

    <p class="subtitle">Why Machines Deliver a Shared Dividend, the Close of Levy Systems,<br>and a Steady Treasury</p>

    <h1 class="title">
      <span class="title-lead">The</span>
      <span class="title-main">Harvester's</span>
      <span class="title-main">Ledger</span>
    </h1>

    <div class="artwork" role="img" aria-label="Illustration of a small thought cloud with an arrow pointing down onto stacks of gold coins"></div>

    <p class="author">Brent Hallow</p>
  </section>
</main>
</body>
</html>
```